Business school needs a web design

Who We are:
KRVT is a small business school that offers programs in Project Management. The school is based in West Africa and welcomes students from the whole area. Our aim is to become one of the reference business schools in Africa.

Project Brief:
The site will include all informations relevant for different types of visitors that we have: actual and future students, companies, mass media, future employees, ect. It will present information about subscription, list of programs, presentation of the school and its team,etc.

What We want:
This competition is for Design only no coding! We need design for two pages.
We did some wireframing for the home page and the list of programs page. We made them just to show how we imagine the website would look like. But we encourage creative designs, so you don't have to stick to the wireframe models.

Sites We like:
http://www.ravenmoorcollege.example/
http://www.belvantis.example/fr/etudes.html
http://www.qtl.example/mba/Pages/default.aspx

Color schemes
The logo of the school is red and black. So the color scheme of the website should match that. For the rest, it is opened to your imagination.
Updates

The payment for the project is now garanteed. Good luck to you all !

Target Market(s)

The target market is diversified because we have students of different ages, also company representatives or employees that might visit the website for recruitment purposes. But the majority of our audience should be aged between 20 - 30 years.

Industry/Entity Type

Small Business

Requirements
Must have
• The design must include two pages: a home page and another interior page : might be the list of programs or any other page relevant to the domain. The Home page must include a slide show at the beginning.
The background page must be white.
Nice to have
• The use of flat design for this project is preferred.
The use of Pelican scaffold as a base for the design is an asset.

```html
<!DOCTYPE html>
<html lang="fr">
<head>
<meta charset="utf-8">
<title>KRVT – Ecole de gestion</title>
<link rel="stylesheet" href="https://fonts.googleapis.com/css2?family=Carlito:wght@400;700&display=swap">
<style>
:root{
  --red:#c00000;
  --ink:#1e1e1e;
  --text:#444;
  --panel:#f3f3f3;
  --footer:#1c1c1c;
  --footer-line:#333;
  --white:#fff;
}
*{box-sizing:border-box;margin:0;padding:0}
html,body{width:818px;height:1200px;overflow:hidden;background:var(--white)}
body{position:relative;font-family:"Carlito",Arial,sans-serif;color:var(--text)}
a{color:inherit;text-decoration:none}
.abs{position:absolute}
.nw{white-space:nowrap}

/* header */
.top-links{left:430px;top:14px;width:298px;text-align:right;font-size:7.5px;color:var(--ink)}
.brand{left:86px;top:38px;display:flex;align-items:center;gap:5px}
.brand-mark{width:12px;height:12px;background:var(--red)}
.brand-name{font-size:16px;font-weight:700;color:var(--ink)}
.main-nav{left:157px;top:42px;font-size:10px;font-weight:700;color:var(--ink);white-space:nowrap}
.main-nav .active{color:var(--red)}
.main-nav .sep{margin:0 4px}
.search{left:624px;top:40px;width:104px;height:18px;border:1px solid #ddd;border-radius:3px;background:#f6f6f6;font-size:7px;color:#aaa;padding:5px 6px}

/* hero */
.hero{left:0;top:74px;width:818px;height:260px;background:linear-gradient(180deg,#6f6b66 0%,#c9c4bb 45%,#8a8278 70%,#2a2622 100%)}
.dots{left:390px;top:302px;display:flex;gap:3px}
.dots span{width:7px;height:7px;background:var(--white)}
.dots span:first-child{background:var(--red)}

/* left column */
.audience{left:86px;top:364px;width:150px;height:176px;background:var(--red);color:var(--white);padding:8px 10px}
.audience h2{font-size:11px;font-weight:700;margin-bottom:0;padding-bottom:3px;border-bottom:1px solid rgba(255,255,255,.25)}
.audience li{list-style:none;font-size:8.5px;line-height:20.2px}
.tv-title{left:86px;top:560px;font-size:11px;font-weight:700;color:var(--ink)}
.tv{left:86px;top:578px;width:150px;height:104px;background:linear-gradient(120deg,#d8dde0,#b9c3c7 55%,#7fae63)}
.play{left:57px;top:44px;width:24px;height:17px;background:rgba(0,0,0,.75);border-radius:2px}
.play::after{content:"";position:absolute;left:9px;top:4px;border-left:7px solid #fff;border-top:4.5px solid transparent;border-bottom:4.5px solid transparent}
.tv-bar{left:4px;bottom:3px;width:142px;height:8px;background:rgba(0,0,0,.7)}
.tv-bar span{position:absolute;left:3px;top:3px;width:30px;height:2px;background:#3a9ad9}

/* centre column */
.intro-title{left:250px;top:362px;font-size:11px;font-weight:700;color:var(--ink)}
.intro{left:250px;top:389px;font-size:8.8px;line-height:16.4px;color:var(--text);white-space:nowrap}
.section-title{font-size:11px;font-weight:700;color:var(--ink)}
.blog-card{width:97px;top:527px}
.blog-img{width:97px;height:60px}
.blog-date{margin-top:15px;font-size:8.5px;font-weight:700;color:var(--ink)}
.blog-head{margin-top:2px;font-size:8.5px;line-height:13.5px;font-weight:700;color:var(--ink)}
.blog-body{margin-top:5px;font-size:7.2px;line-height:13.6px;white-space:nowrap}
.blog-by{font-size:7.2px;line-height:12px}
.blog-more{font-size:8.5px;font-weight:700;color:var(--red);line-height:14px}
.event-date{width:40px;height:37px;background:var(--red);color:var(--white);font-size:10.5px;font-weight:700;text-align:center;line-height:13px;padding-top:5px}
.event-title{font-size:10px;font-weight:700;color:var(--ink)}
.event-text{font-size:7.2px;line-height:13.6px}

/* news */
.news{left:578px;top:364px;width:150px;height:504px;background:var(--panel)}
.news h2{position:absolute;left:8px;top:9px;font-size:11px;font-weight:700;color:var(--ink)}
.news-item{position:absolute;left:8px;display:flex;gap:6px}
.news-img{width:46px;height:33px;flex:none;margin-top:4px}
.news-text{font-size:7px;line-height:13.6px;color:var(--text);white-space:nowrap}
.news-text b{font-weight:400;color:var(--red);display:block}

/* share rail */
.share{left:795px;top:563px;display:flex;flex-direction:column;gap:3px}
.share span{width:23px;height:22px;display:block}

/* partners */
.partners-band{left:0;top:912px;width:818px;height:90px;background:linear-gradient(180deg,#ececec 0%,#fff 20%)}
.partner{top:954px;font-size:19px;font-weight:700;display:flex;align-items:center;gap:5px}
.partner i{width:10px;height:10px;display:block}

/* footer */
.footer{left:0;top:1002px;width:818px;height:198px;background:var(--footer);color:#ddd}
.f-col{position:absolute;top:22px;font-size:8.5px;line-height:16.3px}
.f-col h3{font-size:11px;font-weight:700;color:var(--white);margin-bottom:1px;line-height:14px}
.f-col .strong{font-size:10.5px;font-weight:700;color:var(--white)}
.socials{display:flex;gap:7px;margin-top:8px}
.socials span{width:18px;height:18px;background:#e6e6e6;border-radius:3px}
.phone{display:flex;align-items:center;gap:10px;font-size:11px;font-weight:700;color:var(--white);line-height:20px}
.newsletter-form{position:absolute;left:524px;top:104px;width:204px;height:32px;background:#0d0d0d;border-radius:3px}
.newsletter-form button{position:absolute;right:6px;top:7px;width:54px;height:18px;border:0;border-radius:2px;background:#e9e9e9;font:400 8px "Carlito",Arial,sans-serif;color:#222}
.f-rule{position:absolute;left:0;top:163px;width:818px;height:1px;background:var(--footer-line)}
.copyright{position:absolute;left:86px;top:177px;font-size:7px;color:#ccc}
.f-mark{position:absolute;left:787px;top:173px;font-size:7px;color:#ccc}
</style>
</head>
<body>

<header>
  <nav class="abs top-links">Repertoire du personal | &nbsp;Blogue &nbsp;| Salle de presse | &nbsp;Nous joindre &nbsp;| &nbsp;Francais</nav>
  <div class="abs brand"><span class="brand-mark"></span><span class="brand-name">KRVT</span></div>
  <nav class="abs main-nav"><span class="active">A propos de l'KRVT</span><span class="sep">|</span>Programmes et Formations<span class="sep">|</span>Etuiants<span class="sep">|</span>Nouvelles et Evenements<span class="sep">|</span>Entreprises</nav>
  <div class="abs search">Search</div>
</header>

<section class="abs hero" role="img" aria-label="Slideshow photo: business people silhouetted against a tall office window overlooking a city"></section>
<div class="abs dots"><span></span><span></span><span></span><span></span></div>

<aside>
  <div class="abs audience">
    <h2>Vous etes</h2>
    <ul>
      <li>Futur etudiant</li><li>etudiant actuel</li><li>Enterprise</li><li>employeur</li><li>postulant</li><li>medias</li><li>partnaires</li>
    </ul>
  </div>
  <div class="abs tv-title">KRVT.tv</div>
  <div class="abs tv" role="img" aria-label="Video still: students working at computers in a classroom">
    <span class="abs play"></span>
    <span class="abs tv-bar"><span></span></span>
  </div>
</aside>

<main>
  <h1 class="abs intro-title">KRVT : Devenez les gestionnaires de demain</h1>
  <p class="abs intro">Lorem Ipsum is simply dummy text of the printing and typesetting industry.<br>Lorem Ipsum has been the industry's standard dummy text ever since the 1500s,<br>when an unknown printer took a galley of type and scrambled it to make a type<br>specimen book. It has survived not only five centuries, but also the leap into<br>electronic typesetting, remaining essentially unchanged.</p>

  <h2 class="abs section-title" style="left:252px;top:499px">Blogue</h2>
  <article class="abs blog-card" style="left:250px">
    <div class="blog-img" role="img" aria-label="Photo: group of smiling students" style="background:linear-gradient(135deg,#8a6a4e,#c7a27e 50%,#6d7f8c)"></div>
    <div class="blog-date">Nov ,11,2013</div>
    <div class="blog-head">Lorem Ipsum is simply dummy text</div>
    <p class="blog-body">The printing and typesetting<br>industry. Lorem Ipsum has<br>been the industry's standard<br>dummy text ever</p>
    <div class="blog-by">By Me</div>
    <a class="blog-more">Life la Suite</a>
  </article>
  <article class="abs blog-card" style="left:359px">
    <div class="blog-img" role="img" aria-label="Photo: business team in an office" style="background:linear-gradient(135deg,#dfe6ec,#9fb3c6 50%,#3d4f66)"></div>
    <div class="blog-date">Nov ,11,2013</div>
    <div class="blog-head">Lorem Ipsum is simply dummy text</div>
    <p class="blog-body">The printing and typesetting<br>industry. Lorem Ipsum has<br>been the industry's standard<br>dummy text ever</p>
    <div class="blog-by">By Me</div>
    <a class="blog-more">Life la Suite</a>
  </article>
  <article class="abs blog-card" style="left:467px">
    <div class="blog-img" role="img" aria-label="Photo: students around a laptop" style="background:linear-gradient(135deg,#cfd6da,#8fa0ab 50%,#b44a3c)"></div>
    <div class="blog-date">Nov ,11,2013</div>
    <div class="blog-head">Lorem Ipsum is simply dummy text</div>
    <p class="blog-body">The printing and typesetting<br>industry. Lorem Ipsum has<br>been the industry's standard<br>dummy text ever</p>
    <div class="blog-by">By Me</div>
    <a class="blog-more">Life la Suite</a>
  </article>

  <h2 class="abs section-title" style="left:250px;top:757px">Evenements</h2>
  <div class="abs event-date" style="left:250px;top:780px">NOV<br>2013</div>
  <div class="abs event-title" style="left:305px;top:780px">Event A</div>
  <p class="abs event-text" style="left:306px;top:801px">Lorem Ipsum is simply dummy text of the printing and typesetting industry.<br>Lorem Ipsum has been the industry's standard dummy text ever</p>
  <div class="abs event-date" style="left:250px;top:852px">NOV<br>2013</div>
  <div class="abs event-title" style="left:305px;top:850px">Event B</div>
  <p class="abs event-text" style="left:306px;top:871px">Lorem Ipsum is simply dummy text of the printing and typesetting industry.<br>Lorem Ipsum has been the industry's standard dummy text ever</p>
</main>

<aside class="abs news">
  <h2>News</h2>
  <div class="news-item" style="top:29px"><div class="news-img" role="img" aria-label="Photo: business team" style="background:linear-gradient(135deg,#9aa7b2,#3d4652)"></div><p class="news-text"><b>Lorem ipsum dolor</b>Lorem Ipsum is simply<br>dummy text of the<br>printing and typesetting<br>industry.</p></div>
  <div class="news-item" style="top:106px"><div class="news-img" role="img" aria-label="Photo: laptop on a desk" style="background:linear-gradient(135deg,#2b2f35,#7a8691)"></div><p class="news-text"><b>Lorem ipsum dolor</b>Lorem Ipsum is simply<br>dummy text of the<br>printing and typesetting<br>industry.</p></div>
  <div class="news-item" style="top:182px"><div class="news-img" role="img" aria-label="Photo: woman on the phone" style="background:linear-gradient(135deg,#c9c5c0,#5d5a57)"></div><p class="news-text"><b>Lorem ipsum dolor</b>Lorem Ipsum is simply<br>dummy text of the<br>printing and typesetting<br>industry.</p></div>
  <div class="news-item" style="top:263px"><div class="news-img" role="img" aria-label="Photo: puzzle pieces" style="background:linear-gradient(135deg,#d8a12c,#a3261a)"></div><p class="news-text"><b>Lorem ipsum dolor</b>Lorem Ipsum is simply<br>dummy text of the<br>printing and typesetting<br>industry.</p></div>
  <div class="news-item" style="top:347px"><div class="news-img" role="img" aria-label="Photo: colleagues in a meeting" style="background:linear-gradient(135deg,#e2e6ea,#7c8a99)"></div><p class="news-text"><b>Lorem ipsum dolor</b>Lorem Ipsum is simply<br>dummy text of the<br>printing and typesetting<br>industry.</p></div>
  <div class="news-item" style="top:428px"><div class="news-img" role="img" aria-label="Photo: handshake in an office" style="background:linear-gradient(135deg,#4c5866,#b8c2cc)"></div><p class="news-text"><b>Lorem ipsum dolor</b>Lorem Ipsum is simply<br>dummy text of the<br>printing and typesetting<br>industry.</p></div>
</aside>

<div class="abs share" aria-label="Share tools">
  <span style="background:#3b5a9a"></span>
  <span style="background:#2aa3dd"></span>
  <span style="background:#1676b3"></span>
  <span style="background:#5fb73e"></span>
  <span style="background:#d92222"></span>
</div>

<section class="abs partners-band" aria-label="Partenaires"></section>
<div class="abs partner" style="left:92px;color:#e46d1f"><i style="background:#e46d1f;border-radius:50%"></i>Veltacom</div>
<div class="abs partner" style="left:256px;color:#9a8a17"><i style="background:#9a8a17"></i>Aeronord</div>
<div class="abs partner" style="left:370px;color:#1f7cc1"><i style="background:#1f7cc1"></i>Exportis</div>
<div class="abs partner" style="left:464px;color:#23357d"><i style="background:#23357d"></i>Santea</div>
<div class="abs partner" style="left:548px;color:#222"><i style="background:#c41f1f;border-radius:50%"></i>Provira</div>
<div class="abs partner" style="left:640px;color:#1d3f8a"><i style="background:#d0201e;border-radius:50%"></i>Lumelec</div>

<footer class="abs footer">
  <div class="f-col" style="left:86px">
    <h3>Social Media</h3>
    <div class="socials" aria-label="Social networks"><span></span><span></span><span></span><span></span></div>
  </div>
  <div class="f-col" style="left:195px">
    <h3>A propos</h3>
    A propos de l'KRVT<br>Admissions<br>Calendrier de lecole<br>Offres d emploi<br>Repertoire du personnel
  </div>
  <div class="f-col" style="left:306px">
    <h3>Etudiants</h3>
    Accueil- Etudiants<br>Vie etudeiante<br><span class="strong">Enterprises</span><br><span class="strong">Blogue</span>
  </div>
  <div class="f-col" style="left:391px">
    <h3>KRVT</h3>
    12, Rue des Baobabs<br>Quartier Nord,pres du marche<br>des artisans
    <div class="phone" style="margin-top:8px"><svg width="10" height="12" viewBox="0 0 10 12"><path d="M2 0h2l1 3-1.5 1c.6 1.6 1.5 2.8 2.7 3.8L7.5 7 10 8.5V11c-5 1-10-5-8-11z" fill="#ddd"/></svg>(000) 11 204 30 18</div>
    <div class="phone"><svg width="10" height="12" viewBox="0 0 10 12"><path d="M2 0h2l1 3-1.5 1c.6 1.6 1.5 2.8 2.7 3.8L7.5 7 10 8.5V11c-5 1-10-5-8-11z" fill="#ddd"/></svg>(000) 55 317 42 09</div>
  </div>
  <div class="f-col nw" style="left:523px;width:205px;font-size:7px;line-height:15.2px;top:26px">
    <h3 style="display:flex;align-items:center;gap:5px">Infolettre <svg width="15" height="11" viewBox="0 0 15 11"><rect x=".5" y=".5" width="14" height="10" fill="none" stroke="#fff"/><path d="M.5.5l7 6 7-6" fill="none" stroke="#fff"/></svg></h3>
    Lorem Ipsum is simply dummy text of the printing and<br>typesetting industry. Lorem Ipsum has been the industry's<br>standard dummy text ever since the 1500s, when an<br>unknown printer
  </div>
  <form class="newsletter-form"><button type="button">ENVOYER</button></form>
  <div class="f-rule"></div>
  <p class="copyright">Copyright ©2013 Company Name &nbsp;- All rights reserved</p>
  <span class="f-mark">CS</span>
</footer>

</body>
</html>
```